" Empresa que atua há mais de 15 anos fabricando capas de sofás, almofadas, pufes e etc. Hoje fabricamos sofás, poltronas, pufes além de estofarmos estes móveis. www.ateliedosforros.com.br "

```html
<!DOCTYPE html>
<html lang="pt-BR">
<head>
<meta charset="utf-8">
<title>Ateliê dos Forros — Cartão de visita</title>
<link rel="stylesheet" href="https://fonts.googleapis.com/css2?family=Poiret+One&family=Montserrat:wght@300;400&display=swap">
<style>
  :root {
    --canvas: #e9ebee;
    --card: #ffffff;
    --brand: #1f5a8a;
    --brand-dot: #3a9fd8;
    --ink: #333a40;
    --ink-soft: #5b636a;
    --blue-deep: #1f6fb8;
    --blue-light: #5ec3ec;
  }
  * { margin: 0; padding: 0; box-sizing: border-box; }
  html, body { width: 1200px; height: 1200px; overflow: hidden; }
  body {
    background: var(--canvas);
    display: flex;
    flex-direction: column;
    align-items: center;
    justify-content: center;
    gap: 60px;
    font-family: "Montserrat", sans-serif;
  }
  .card {
    position: relative;
    width: 900px;
    height: 500px;
    background: var(--card);
    border-radius: 36px;
    overflow: hidden;
    box-shadow: 0 6px 24px rgba(0,0,0,0.12);
  }
  .brand {
    display: flex;
    align-items: center;
    gap: 16px;
    font-family: "Poiret One", sans-serif;
    color: var(--brand);
    white-space: nowrap;
  }
  .brand-dot {
    flex: none;
    border-radius: 50%;
    background: var(--brand-dot);
  }
  .card-back {
    display: flex;
    align-items: center;
    justify-content: center;
  }
  .card-back .brand { font-size: 52px; }
  .card-back .brand-dot { width: 44px; height: 44px; }
  .card-front .brand {
    position: absolute;
    left: 44px;
    top: 62px;
    font-size: 38px;
  }
  .card-front .brand-dot { width: 32px; height: 32px; }
  .role {
    position: absolute;
    left: 476px;
    top: 104px;
    font-size: 26px;
    font-weight: 400;
    color: var(--ink);
  }
  .contact {
    position: absolute;
    left: 510px;
    top: 190px;
    list-style: none;
    font-size: 17px;
    font-weight: 300;
    color: var(--ink-soft);
    line-height: 1.75;
  }
  .decor-band {
    position: absolute;
    left: 0;
    bottom: 0;
    width: 900px;
    height: 160px;
    background: linear-gradient(90deg, var(--blue-deep), var(--blue-light));
  }
</style>
</head>
<body>
  <section class="card card-back" aria-label="Verso do cartão">
    <div class="brand"><span class="brand-dot"></span><span class="brand-name">Ateliê dos Forros</span></div>
  </section>

  <section class="card card-front" aria-label="Frente do cartão">
    <div class="brand"><span class="brand-dot"></span><span class="brand-name">Ateliê dos Forros</span></div>
    <p class="role">Nome | Função</p>
    <ul class="contact">
      <li>Telefone: 0000-0000</li>
      <li>Celular: 0000-0000</li>
      <li>Email: contato@contato.com.br</li>
    </ul>
    <div class="decor-band" role="img" aria-label="Faixa decorativa em tons de azul na base do cartão"></div>
  </section>
</body>
</html>
```